STATIONERY FOR OUR CLIENT

I have a client that is a major oilseed processor in Australia. They want a deluxe gorgeous version of their business card.
I am proposing we print the business cards in Pelbrix.com VARNO versions with the coloured edging, probably in black. Their business name needs to appear on both sides whether in logo or text.
The stationery needs to be layed up to look lifelike to impress the client. Ideally full stationery including letterhead, business card, with compliments, envelopes.
We want to impress our client.
*** The design needs to communicate - quality, premium, prestige, modern, expert, wealthy, abundant, sophisticated, established.
Designs need to be not too dark, not alot of black please. Clean, modern, sophisticated, upmarket, luxury brand.
I need 3 concepts to present to client and once approved, refined to then have print ready files - and working files just in case we have to make tweaks down the track.
We also need to create a one page style guide, that includes pms colour etc.
THIS IS AN URGENT JOB
Updates

Please design less with black more with clean white possibly light grey/beige as secondary colour if you are looking for contrast. I have added some examples of cards that look nice and might help with what the client is looking for. thank you and looking forward to seeing the designs

Please ensure all designs submitted have the correct contact details of our client which is in the brief. Also please do not have any black backgrounds - if any of your design do have black backgrounds, please amend. Thank you

Target Market(s)

business customers, investors, major distributors

Industry/Entity Type

Business

Font styles to use
Sans Serif

Requirements
Must have
• must have business name on both sides. designed to be printed with pelbrix.com using their VARNO business card print offering.
Should not have
• alot of black

```html
<!DOCTYPE html>
<html lang="en">
<head>
<meta charset="utf-8">
<title>KALO – Business Card</title>
<link rel="stylesheet" href="https://fonts.googleapis.com/css2?family=Montserrat:wght@400;500;600;700&display=swap">
<style>
  :root {
    --backdrop: #e6e6e4;
    --card: #ffffff;
    --ink: #1c1c1c;
    --ink-soft: #3a3a3a;
    --green: #3fa56f;
    --on-green: #ffffff;
  }
  * { box-sizing: border-box; margin: 0; padding: 0; }
  html, body {
    width: 1200px;
    height: 873px;
    overflow: hidden;
  }
  body {
    background: var(--backdrop);
    font-family: "Montserrat", sans-serif;
    color: var(--ink);
    position: relative;
  }
  .card {
    position: absolute;
    top: 278px;
    width: 520px;
    height: 316px;
    background: var(--card);
    box-shadow: 0 2px 6px rgba(0,0,0,0.12);
    overflow: hidden;
  }
  .card--front { left: 50px; }
  .card--back { left: 630px; }

  /* Front */
  .company {
    position: absolute;
    left: 60px;
    top: 96px;
  }
  .company__name {
    font-size: 88px;
    font-weight: 700;
    letter-spacing: 8px;
    line-height: 1;
    color: var(--ink);
  }
  .company__tagline {
    margin-top: 14px;
    white-space: nowrap;
    font-size: 17px;
    font-weight: 500;
    letter-spacing: 0.5px;
    color: var(--ink);
  }

  /* Back */
  .brand-band {
    position: absolute;
    left: 0;
    top: 0;
    width: 100%;
    height: 66px;
    background: var(--green);
    display: flex;
    align-items: center;
    padding-left: 28px;
  }
  .brand-band__name {
    font-size: 36px;
    font-weight: 600;
    letter-spacing: 6px;
    color: var(--on-green);
  }
  .person {
    position: absolute;
    left: 28px;
    top: 92px;
  }
  .person__name {
    font-size: 21px;
    font-weight: 700;
    letter-spacing: 0.5px;
  }
  .person__title {
    margin-top: 3px;
    font-size: 10px;
    color: var(--ink-soft);
  }
  .contact {
    position: absolute;
    left: 226px;
    top: 86px;
    list-style: none;
    font-size: 12.5px;
    line-height: 16.5px;
    color: var(--ink);
  }
</style>
</head>
<body>
  <section class="card card--front" aria-label="Business card front">
    <div class="company">
      <p class="company__name">KALO</p>
      <p class="company__tagline">Wirralee Oils &amp; Bioenergy</p>
    </div>
  </section>

  <section class="card card--back" aria-label="Business card back">
    <header class="brand-band">
      <span class="brand-band__name">KALO</span>
    </header>
    <div class="person">
      <p class="person__name">R.J. Halden</p>
      <p class="person__title">Managing Director</p>
    </div>
    <ul class="contact">
      <li>Unit 5, 48 Calder Street</li>
      <li>Fernvale VIC 2140</li>
      <li>03 9555 0142</li>
      <li>0400 555 317</li>
      <li>hello@wirraleeoils.com.au</li>
      <li>wirraleeoils.com.au</li>
      <li>pagebook.net/wirraleeoils</li>
    </ul>
  </section>
</body>
</html>
```